PowerPoint Template for Quandel

Cover Page, Table of Contents Page, and slide template that can be incorporated into table of contents, in an editable form. Using attached logo.

```html
<!DOCTYPE html>
<html lang="en">
<head>
<meta charset="utf-8">
<title>Quandel – Presentation Template</title>
<link href="https://fonts.googleapis.com/css2?family=Questrial&display=swap" rel="stylesheet">
<style>
:root{
  --teal:#1fb2b5;
  --teal-deep:#139fa8;
  --teal-soft:#5cc9c6;
  --green:#7dbb42;
  --lime:#b6d64a;
  --white:#ffffff;
  --ink:#555a5e;
  --muted:#9a9ea2;
  --line:#e2e5e6;
  --canvas:#f1f2f2;
  --chart-bg:#cfd2d3;
}
*{box-sizing:border-box;margin:0;padding:0}
html,body{width:1200px;height:2386px;overflow:hidden;background:var(--canvas)}
body{font-family:"Questrial",sans-serif;color:var(--ink)}
.deck{
  width:1200px;height:2386px;padding:6px 9px 0 8px;
  display:grid;grid-template-columns:583px 583px;grid-auto-rows:327px;
  column-gap:17px;row-gap:13px;
}
.slide{position:relative;overflow:hidden;background:var(--white)}
.abs{position:absolute}
.photo{position:absolute;inset:0}

/* logo wordmark */
.wordmark{position:absolute;font-size:22px;letter-spacing:3px;color:var(--white);line-height:1}
.wordmark.small{font-size:12px;letter-spacing:1.6px;color:var(--teal)}

/* cover typography */
.cover-title{position:absolute;color:var(--white);font-size:28px;line-height:1.2;letter-spacing:.3px}
.cover-sub{position:absolute;color:var(--white);font-size:11px}
.site{position:absolute;color:var(--white);font-size:9px}

/* decorative dots */
.dot{position:absolute;border-radius:50%;background:var(--lime);opacity:.7}

/* content slides */
.heading{position:absolute;left:36px;top:28px;font-size:20px;color:var(--teal);letter-spacing:.5px}
.heading-rule{position:absolute;left:36px;top:56px;width:26px;height:2px;background:var(--green)}
.footer-copy{position:absolute;left:0;right:0;top:296px;text-align:center;font-size:4.5px;color:var(--muted)}
.footer-dots{position:absolute;left:50%;top:309px;transform:translateX(-50%);display:flex;gap:6px}
.footer-dots span{width:5px;height:5px;border-radius:50%;background:var(--green)}
.page-num{position:absolute;left:539px;top:287px;width:14px;height:14px;border-radius:50%;background:var(--green);color:var(--white);font-size:7px;display:flex;align-items:center;justify-content:center}
.footer-logo{left:34px;top:290px}

/* team */
.portrait{position:absolute;width:108px;height:107px;border:4px solid var(--teal);border-radius:50% 50% 50% 6px;box-shadow:0 0 0 2px var(--white),0 0 0 3px var(--teal-soft)}
.portrait.alt{border-radius:50% 50% 6px 50%;border-color:var(--green);box-shadow:0 0 0 2px var(--white),0 0 0 3px var(--lime)}
.member-name{position:absolute;font-size:14px;color:#a6aaad}
.member-text{position:absolute;width:240px;font-size:6.4px;line-height:1.4;color:var(--muted)}
.role{position:absolute;height:14px;padding:0 14px;border-radius:7px;background:linear-gradient(90deg,var(--teal),var(--green));color:var(--white);font-size:7px;line-height:14px}
.team-pill{position:absolute;height:62px;background:var(--teal);color:var(--white);font-size:23px;display:flex;align-items:center}
.connector{position:absolute;height:1px;background:#bfc3c5}

/* text area */
.body-copy{position:absolute;left:36px;top:76px;width:516px;font-size:6.6px;line-height:1.38;color:var(--muted);text-align:justify}
.body-copy p+p{margin-top:7px}

/* quadrant */
.quad-box{position:absolute;width:100px;height:62px;border:1px solid #c8cbcd;background:var(--white);padding:4px;box-shadow:0 2px 4px rgba(0,0,0,.18)}
.quad-box div{width:100%;height:100%;color:var(--white);text-align:center;font-size:8px;padding-top:10px;line-height:1.3}
.quad-box b{display:block;font-weight:normal;font-size:9px}
.qi{position:absolute;left:405px;display:flex;gap:12px;align-items:flex-start}
.qi-icon{width:25px;height:25px;border-radius:50%;display:flex;align-items:center;justify-content:center}
.qi-text{font-size:6.4px;line-height:1.35;color:var(--muted);width:100px}
.qi-text b{display:block;font-weight:normal;font-size:8px;color:#a6aaad}

/* stats */
.stat-card{position:absolute;left:42px;top:76px;width:110px;height:200px;background:var(--white);box-shadow:0 1px 5px rgba(0,0,0,.18);padding:18px 12px}
.stat-num{font-size:26px;color:var(--teal)}
.stat-label{font-size:8px;color:var(--ink);margin-top:2px}
.stat-desc{font-size:6.4px;color:var(--muted);line-height:1.35;margin:6px 0 14px}

/* toc */
.toc-row{display:flex;justify-content:space-between;font-size:6.6px;color:var(--ink);padding:7px 0;border-bottom:1px solid var(--line)}
</style>
</head>
<body>
<main class="deck">

  <!-- 1 teal cover -->
  <section class="slide">
    <div class="photo" role="img" aria-label="Teal-tinted photo of a doctor writing at a desk" style="background:linear-gradient(120deg,#29b5b6 0%,#3bbcbb 45%,#1fa9b2 100%)"></div>
    <div class="wordmark" style="left:38px;top:52px">QUANDEL</div>
    <h1 class="cover-title" style="left:38px;top:120px">YOUR PRESENTATION<br>TITLE GOES HERE</h1>
    <p class="cover-sub" style="left:38px;top:196px">YOUR TITLE GOES HERE</p>
    <p class="site" style="left:38px;top:272px">www.yourwebsite.com</p>
    <span class="dot" style="left:304px;top:232px;width:44px;height:44px"></span>
    <span class="dot" style="left:218px;top:278px;width:56px;height:56px"></span>
    <span class="dot" style="left:400px;top:252px;width:30px;height:30px"></span>
    <span class="dot" style="left:466px;top:236px;width:30px;height:30px"></span>
    <span class="dot" style="left:510px;top:276px;width:22px;height:22px"></span>
    <span class="dot" style="left:556px;top:312px;width:18px;height:18px"></span>
  </section>

  <!-- 2 white cover -->
  <section class="slide">
    <div class="photo" role="img" aria-label="Faded pale photo of a doctor at work" style="background:linear-gradient(120deg,#f4f6f6 0%,#eef1f1 50%,#ffffff 100%)"></div>
    <div class="wordmark" style="right:30px;left:auto;top:44px;color:var(--teal)">QUANDEL</div>
    <h1 class="cover-title" style="right:28px;top:124px;text-align:right;color:var(--teal)">YOUR PRESENTATION<br>TITLE GOES HERE</h1>
    <p class="cover-sub" style="right:28px;top:212px;color:var(--teal)">YOUR TITLE GOES HERE</p>
    <p class="site" style="right:28px;top:294px;color:var(--teal)">www.yourwebsite.com</p>
    <span class="dot" style="left:-18px;top:250px;width:70px;height:70px"></span>
    <span class="dot" style="left:54px;top:228px;width:44px;height:44px;background:var(--green)"></span>
    <span class="dot" style="left:118px;top:258px;width:36px;height:36px;background:var(--green)"></span>
    <span class="dot" style="left:220px;top:232px;width:32px;height:32px;background:var(--green)"></span>
    <span class="dot" style="left:168px;top:296px;width:22px;height:22px;background:var(--green)"></span>
  </section>

  <!-- 3 green cover -->
  <section class="slide">
    <div class="photo" role="img" aria-label="Green and teal tinted photo of a pharmacy shelf" style="background:linear-gradient(115deg,#8cc544 0%,#58b886 45%,#25aeb2 100%)"></div>
    <div class="wordmark" style="left:38px;top:52px">QUANDEL</div>
    <h1 class="cover-title" style="left:38px;top:120px">YOUR PRESENTATION<br>TITLE GOES HERE</h1>
    <p class="cover-sub" style="left:38px;top:196px">Your Title Goes Here</p>
    <p class="site" style="left:38px;top:272px">www.yourwebsite.com</p>
    <span class="dot" style="left:304px;top:232px;width:44px;height:44px"></span>
    <span class="dot" style="left:218px;top:278px;width:56px;height:56px"></span>
    <span class="dot" style="left:400px;top:252px;width:30px;height:30px"></span>
    <span class="dot" style="left:466px;top:236px;width:30px;height:30px"></span>
    <span class="dot" style="left:510px;top:276px;width:22px;height:22px"></span>
    <span class="dot" style="left:556px;top:312px;width:18px;height:18px"></span>
  </section>

  <!-- 4 table of contents -->
  <section class="slide">
    <div class="abs" role="img" aria-label="Teal tinted photo of medicine bottles" style="left:0;top:0;width:306px;height:327px;background:linear-gradient(130deg,#2cb5b4 0%,#1faab0 60%,#36b7a0 100%)"></div>
    <h2 class="abs" style="left:58px;top:70px;color:var(--white);font-size:17px;font-weight:normal">TABLE OF CONTENTS</h2>
    <div class="wordmark" style="left:96px;top:152px;font-size:24px">QUANDEL</div>
    <span class="dot" style="left:30px;top:258px;width:40px;height:40px"></span>
    <span class="dot" style="left:112px;top:270px;width:38px;height:38px"></span>
    <span class="dot" style="left:196px;top:254px;width:26px;height:26px"></span>
    <span class="dot" style="left:248px;top:290px;width:20px;height:20px"></span>
    <div class="abs" style="left:278px;top:88px;width:290px;height:196px;background:var(--white);padding:4px 14px;box-shadow:-2px 2px 6px rgba(0,0,0,.12)">
      <div class="toc-row"><span>These are scientific commentaries</span><span>01</span></div>
      <div class="toc-row"><span>Second Row These are scientific commentaries</span><span>02</span></div>
      <div class="toc-row"><span>Third Row These are scientific commentaries</span><span>03</span></div>
      <div class="toc-row"><span>Fourth Row These are scientific commentaries</span><span>04</span></div>
      <div class="toc-row"><span>Fifth Row These are scientific commentaries</span><span>20</span></div>
      <div class="toc-row"><span>Sixth Row These are scientific commentaries</span><span>21</span></div>
      <div class="toc-row"><span>Last Row These are scientific commentaries</span><span>31</span></div>
      <div class="toc-row" style="border:0"><span>These are scientific commentaries</span><span style="font-size:11px">35</span></div>
    </div>
  </section>

  <!-- 5 header slide -->
  <section class="slide">
    <div class="photo" role="img" aria-label="Photo of white tablets spilling from an amber pill bottle" style="background:linear-gradient(100deg,#e8ecec 0%,#dfe4e4 45%,#f1d7a8 75%,#e8a63a 90%,#f3efe6 100%)"></div>
    <div class="abs" style="left:106px;top:30px;width:382px;height:76px;background:var(--teal);opacity:.92"></div>
    <div class="abs" style="left:296px;top:30px;width:192px;height:76px;background:var(--teal-deep)"></div>
    <div class="wordmark" style="left:124px;top:57px">QUANDEL</div>
    <h2 class="abs" style="left:312px;top:36px;color:var(--white);font-size:16px;font-weight:normal;line-height:1.15">YOUR<br>AWESOME<br>HEADER HERE</h2>
  </section>

  <!-- 6 team right -->
  <section class="slide">
    <div class="portrait" role="img" aria-label="Portrait photo of the co-founder" style="left:43px;top:43px;background:#8a7c74"></div>
    <div class="portrait" role="img" aria-label="Portrait photo of the manager" style="left:43px;top:165px;background:#9a9a98"></div>
    <p class="member-name" style="left:172px;top:66px">Name Here</p>
    <p class="member-text" style="left:172px;top:88px">Ut wisi enim ad minim veniam, quis nostrud exerci tation ullamcorper suscipit lobortis nisl ut aliquip ex ea commodo consequat. Lorem ipsum dolor sit amet.</p>
    <span class="role" style="left:172px;top:129px">CO Founder</span>
    <p class="member-name" style="left:172px;top:180px">Name Here</p>
    <p class="member-text" style="left:172px;top:202px">Ut wisi enim ad minim veniam, quis nostrud exerci tation ullamcorper suscipit lobortis nisl ut aliquip ex ea commodo consequat. Lorem ipsum dolor sit amet.</p>
    <span class="role" style="left:172px;top:243px">Manager</span>
    <div class="connector" style="left:300px;top:165px;width:90px"></div>
    <div class="team-pill" style="left:388px;top:134px;width:195px;border-radius:31px 0 0 31px;padding-left:40px">Our Team</div>
    <div class="wordmark small footer-logo abs">QUANDEL</div>
    <p class="footer-copy">© 2024 QUANDEL. All rights reserved</p>
    <div class="footer-dots"><span></span><span></span><span></span><span></span><span></span><span></span></div>
    <span class="page-num">6</span>
  </section>

  <!-- 7 team left -->
  <section class="slide">
    <div class="team-pill" style="left:0;top:140px;width:206px;border-radius:0 31px 31px 0;padding-left:36px">Our Team</div>
    <div class="connector" style="left:206px;top:171px;width:214px"></div>
    <p class="member-name" style="right:166px;top:66px">Name Here</p>
    <p class="member-text" style="left:178px;top:88px;text-align:right">Ut wisi enim ad minim veniam, quis nostrud exerci tation ullamcorper suscipit lobortis nisl ut aliquip ex ea commodo consequat. Lorem ipsum dolor sit amet.</p>
    <span class="role" style="left:338px;top:129px">Designer</span>
    <p class="member-name" style="right:166px;top:182px">Name Here</p>
    <p class="member-text" style="left:178px;top:204px;text-align:right">Ut wisi enim ad minim veniam, quis nostrud exerci tation ullamcorper suscipit lobortis nisl ut aliquip ex ea commodo consequat. Lorem ipsum dolor sit amet.</p>
    <span class="role" style="left:335px;top:245px">Programer</span>
    <div class="portrait alt" role="img" aria-label="Portrait photo of the designer" style="left:434px;top:45px;background:#c9a688"></div>
    <div class="portrait alt" role="img" aria-label="Portrait photo of the programmer" style="left:434px;top:167px;background:#a98a78"></div>
    <div class="wordmark small footer-logo abs">QUANDEL</div>
    <p class="footer-copy">© 2024 QUANDEL. All rights reserved</p>
    <div class="footer-dots"><span></span><span></span><span></span><span></span><span></span><span></span></div>
    <span class="page-num">7</span>
  </section>

  <!-- 8 text area -->
  <section class="slide">
    <h2 class="heading" style="font-weight:normal">Text Area</h2>
    <span class="heading-rule"></span>
    <div class="body-copy">
      <p>Lorem Ipsum is simply dummy text of the printing and typesetting industry. Lorem Ipsum has been the industry's standard dummy text ever since the 1500s, when an unknown printer took a galley of type and scrambled it to make a type specimen book. It has survived not only five centuries, but also the leap into electronic typesetting, remaining essentially unchanged. It was popularised in the 1960s with the release of transfer sheets containing Lorem Ipsum passages, and more recently with desktop publishing software including versions of Lorem Ipsum.</p>
      <p>Lorem Ipsum is simply dummy text of the printing and typesetting industry. Lorem Ipsum has been the industry's standard dummy text ever since the 1500s, when an unknown printer took a galley of type and scrambled it to make a type specimen book. It has survived not only five centuries, but also the leap into electronic typesetting, remaining essentially unchanged. It was popularised in the 1960s with the release of transfer sheets containing Lorem Ipsum passages, and more recently with desktop publishing software including versions of Lorem Ipsum.</p>
      <p>Lorem Ipsum is simply dummy text of the printing and typesetting industry. Lorem Ipsum has been the industry's standard dummy text ever since the 1500s, when an unknown printer took a galley of type and scrambled it to make a type specimen book. It has survived not only five centuries, but also the leap into electronic typesetting, remaining essentially unchanged. It was popularised in the 1960s with the release of transfer sheets containing Lorem Ipsum passages, and more recently with desktop publishing software including versions of Lorem Ipsum.</p>
      <p>Lorem Ipsum is simply dummy text of the printing and typesetting industry. Lorem Ipsum has been the industry's standard dummy text ever since the 1500s, when an unknown printer took a galley of type and scrambled it to make a type specimen book. It has survived not only five centuries, but also the leap into electronic typesetting, remaining essentially unchanged. It was popularised in the 1960s with the release of transfer sheets containing Lorem Ipsum passages, and more recently with desktop publishing software including versions of Lorem Ipsum.</p>
    </div>
    <div class="wordmark small footer-logo abs">QUANDEL</div>
    <span class="page-num">8</span>
  </section>

  <!-- 9 quadrant boxes -->
  <section class="slide">
    <h2 class="heading" style="font-weight:normal;font-size:18px">QUADRANT AREA</h2>
    <span class="heading-rule"></span>
    <svg class="abs" style="left:32px;top:66px" width="350" height="214" viewBox="0 0 350 214" aria-hidden="true">
      <g fill="none" stroke="#c3c7c9" stroke-width="1">
        <line x1="12" y1="10" x2="12" y2="200"/>
        <line x1="12" y1="200" x2="336" y2="200"/>
        <line x1="174" y1="16" x2="174" y2="192"/>
        <line x1="20" y1="106" x2="330" y2="106"/>
        <circle cx="12" cy="8" r="5"/><circle cx="342" cy="200" r="5"/><circle cx="12" cy="200" r="5"/>
        <path d="M9 8h6M12 5v6M339 200h6M342 197v6M9 200h6"/>
      </g>
    </svg>
    <div class="quad-box" style="left:88px;top:90px"><div style="background:var(--green)"><b>Your Text</b>Lorem ipsum<br>dolor sit amet.</div></div>
    <div class="quad-box" style="left:232px;top:90px"><div style="background:#b3b6b8"><b>Your Text</b>Lorem ipsum<br>dolor sit amet.</div></div>
    <div class="quad-box" style="left:88px;top:182px"><div style="background:var(--teal)"><b>Your Text</b>Lorem ipsum<br>dolor sit amet.</div></div>
    <div class="quad-box" style="left:232px;top:182px"><div style="background:var(--teal-deep)"><b>Your Text</b>Lorem ipsum<br>dolor sit amet.</div></div>
    <p class="abs" style="left:124px;top:272px;font-size:5.5px;color:var(--muted)">Lorem ipsum dolor sit amet, consectetur adipiscing elit</p>
    <div class="qi" style="top:92px"><span class="qi-icon" style="background:var(--green)"><svg width="12" height="12" viewBox="0 0 12 12"><path d="M2 10V7M5 10V4M8 10V6M11 10V2" stroke="#fff" stroke-width="1.6"/></svg></span><p class="qi-text"><b>Your Text</b>Lorem ipsum dolor sit amet, consectetur adipiscing elit</p></div>
    <div class="qi" style="top:140px"><span class="qi-icon" style="background:#e7e9ea"><svg width="12" height="12" viewBox="0 0 12 12"><circle cx="6" cy="6" r="4" fill="none" stroke="#b3b6b8" stroke-width="1.4"/></svg></span><p class="qi-text"><b>Your Text</b>Lorem ipsum dolor sit amet, consectetur adipiscing elit</p></div>
    <div class="qi" style="top:188px"><span class="qi-icon" style="background:var(--teal)"><svg width="12" height="12" viewBox="0 0 12 12"><rect x="2" y="2" width="8" height="6" fill="none" stroke="#fff" stroke-width="1.4"/><path d="M6 8v3" stroke="#fff" stroke-width="1.4"/></svg></span><p class="qi-text"><b>Your Text</b>Lorem ipsum dolor sit amet, consectetur adipiscing elit</p></div>
    <div class="qi" style="top:236px"><span class="qi-icon" style="background:#e7e9ea"><svg width="12" height="12" viewBox="0 0 12 12"><path d="M2 3h8v6H2z" fill="none" stroke="#b3b6b8" stroke-width="1.4"/></svg></span><p class="qi-text"><b>Your Text</b>Lorem ipsum dolor sit amet, consectetur adipiscing elit</p></div>
    <div class="wordmark small footer-logo abs">QUANDEL</div>
    <p class="footer-copy">© 2024 QUANDEL. All rights reserved</p>
    <div class="footer-dots"><span></span><span></span><span></span><span></span><span></span><span></span></div>
    <span class="page-num">9</span>
  </section>

  <!-- 10 quadrant chart -->
  <section class="slide">
    <h2 class="heading" style="font-weight:normal;font-size:18px">QUADRANT AREA</h2>
    <span class="heading-rule"></span>
    <div class="abs" role="img" aria-label="Greyscale photo of medicine behind the chart" style="left:172px;top:66px;width:384px;height:206px;background:linear-gradient(120deg,#d6d8d9,#c5c8c9 60%,#b9bcbd)"></div>
    <svg class="abs" style="left:172px;top:66px" width="384" height="206" viewBox="0 0 384 206" aria-label="Line chart of income and outcome from 2010 to 2015">
      <g font-size="6" fill="#7f8386" font-family="Questrial, sans-serif">
        <text x="8" y="20">4.5</text><text x="8" y="40">4.0</text><text x="8" y="60">3.5</text><text x="8" y="80">3.0</text><text x="8" y="100">2.5</text><text x="8" y="120">2.0</text><text x="8" y="140">1.5</text><text x="8" y="160">1.0</text><text x="8" y="180">0.5</text>
        <text x="44" y="198">2010</text><text x="100" y="198">2011</text><text x="156" y="198">2012</text><text x="212" y="198">2013</text><text x="268" y="198">2014</text><text x="324" y="198">2015</text>
      </g>
      <polyline points="52,140 108,130 164,110 220,100 276,68 332,38" fill="none" stroke="var(--teal)" stroke-width="1.6"/>
      <polyline points="52,122 108,148 164,100 220,116 276,54 332,46" fill="none" stroke="#ffffff" stroke-width="1.4"/>
      <g fill="#fff"><circle cx="52" cy="122" r="2.4"/><circle cx="108" cy="148" r="2.4"/><circle cx="164" cy="100" r="2.4"/><circle cx="220" cy="116" r="2.4"/><circle cx="276" cy="54" r="2.4"/><circle cx="332" cy="46" r="2.4"/></g>
    </svg>
    <div class="stat-card">
      <p class="stat-num">93%</p>
      <p class="stat-label">Income</p>
      <p class="stat-desc">Lorem ipsum is simply dummy text of the printing.</p>
      <p class="stat-num">72%</p>
      <p class="stat-label">Outcome</p>
      <p class="stat-desc">Lorem ipsum is simply dummy text of the printing.</p>
    </div>
    <div class="wordmark small footer-logo abs">QUANDEL</div>
    <p class="footer-copy">© 2024 QUANDEL. All rights reserved</p>
    <div class="footer-dots"><span></span><span></span><span></span><span></span><span></span><span></span></div>
    <span class="page-num">10</span>
  </section>

  <!-- 11 quote -->
  <section class="slide">
    <div class="photo" role="img" aria-label="Teal tinted photo of a doctor writing notes" style="background:linear-gradient(120deg,#2bb4b4 0%,#3dbcbc 50%,#22abb1 100%)"></div>
    <span class="abs" style="left:58px;top:42px;color:var(--white);font-size:52px;line-height:1">“</span>
    <p class="abs" style="left:62px;top:112px;width:430px;color:var(--white);font-size:23px;line-height:1.3">Information is the oil of the 21st century, and analytics is the combustion engine</p>
    <div class="abs" style="left:70px;top:242px;width:200px;height:1px;background:rgba(255,255,255,.7)"></div>
    <p class="abs" style="left:280px;top:237px;color:var(--white);font-size:10px">Martin Hollis, <span style="font-size:8px">Northgate Research</span></p>
  </section>

  <!-- 12 divider band -->
  <section class="slide">
    <div class="photo" role="img" aria-label="Green tinted photo of a prescription pad and stethoscope" style="background:linear-gradient(120deg,#a6cf5a 0%,#8cc54d 50%,#79bb47 100%)"></div>
    <div class="abs" style="left:0;top:150px;width:420px;height:56px;background:var(--teal)"></div>
    <h2 class="abs" style="left:58px;top:162px;color:var(--white);font-size:25px;font-weight:normal">DIVIDER TITLE HERE</h2>
    <div class="abs" style="left:354px;top:140px;width:80px;height:80px;border-radius:50%;background:var(--teal);border:3px solid var(--white);display:flex;align-items:center;justify-content:center">
      <svg width="30" height="30" viewBox="0 0 30 30" aria-hidden="true"><circle cx="15" cy="15" r="13" fill="var(--white)"/><path d="M13 22V8l7 3-7 3" fill="var(--green)" stroke="var(--green)" stroke-width="1.4" stroke-linejoin="round"/><ellipse cx="15" cy="22" rx="5" ry="1.5" fill="none" stroke="var(--teal)" stroke-width="1"/></svg>
    </div>
  </section>

  <!-- 13 teal divider -->
  <section class="slide">
    <div class="photo" style="background:var(--teal)"></div>
    <div class="wordmark" style="left:38px;top:52px">QUANDEL</div>
    <h2 class="cover-title" style="left:38px;top:124px;font-weight:normal">YOUR DIVIDER TITLE<br>GOES HERE</h2>
    <p class="cover-sub" style="left:38px;top:196px">YOUR TITLE GOES HERE</p>
    <p class="site" style="left:38px;top:272px">www.yourwebsite.com</p>
    <span class="dot" style="left:304px;top:232px;width:44px;height:44px"></span>
    <span class="dot" style="left:218px;top:278px;width:56px;height:56px"></span>
    <span class="dot" style="left:400px;top:252px;width:30px;height:30px"></span>
    <span class="dot" style="left:466px;top:236px;width:30px;height:30px"></span>
    <span class="dot" style="left:510px;top:276px;width:22px;height:22px"></span>
    <span class="dot" style="left:556px;top:312px;width:18px;height:18px"></span>
  </section>

  <!-- 14 thank you -->
  <section class="slide">
    <div class="photo" role="img" aria-label="Green and teal tinted photo of a clinic with a wall clock" style="background:linear-gradient(115deg,#7dc04a 0%,#4fb78c 45%,#26aeb1 100%)"></div>
    <div class="wordmark" style="left:38px;top:46px">QUANDEL</div>
    <h2 class="cover-title" style="left:38px;top:146px;font-weight:normal">THANK YOU…</h2>
    <p class="site" style="left:38px;top:192px;font-size:9px;display:flex;align-items:center;gap:8px"><svg width="10" height="8" viewBox="0 0 10 8" aria-hidden="true"><rect x=".5" y=".5" width="9" height="7" fill="none" stroke="#fff"/><path d="M.5 .5 5 4.5 9.5 .5" fill="none" stroke="#fff"/></svg>emailaddress@email.com</p>
    <p class="site" style="left:38px;top:214px;font-size:9px;display:flex;align-items:center;gap:8px"><svg width="10" height="10" viewBox="0 0 10 10" aria-hidden="true"><circle cx="5" cy="5" r="4.5" fill="#fff"/></svg>www.website-address.com</p>
    <p class="site" style="left:38px;top:288px">www.yourwebsite.com</p>
    <span class="dot" style="left:290px;top:260px;width:44px;height:44px"></span>
    <span class="dot" style="left:218px;top:292px;width:52px;height:52px"></span>
    <span class="dot" style="left:390px;top:268px;width:30px;height:30px"></span>
    <span class="dot" style="left:470px;top:252px;width:30px;height:30px"></span>
    <span class="dot" style="left:520px;top:286px;width:22px;height:22px"></span>
  </section>

</main>
</body>
</html>
```